Real Estate Company Needs Stationery Design Project, Logo Redesign, For Sale Design

We are a real estate company in San Diego California. We handle mostly coastal areas with middle to high end properties. Our colors are gray, dark silver, and black. I do not want anything Cartoon-ish but it does need to have a modern feel. We are looking to have these items below designed. We have a logo that we like and we have already built some name recognition so I don’t want to change the design but I am open to it… so feel free to pitch a new logo if you would like. We do however need our logo designed by a pro and put into high resolution Illustrator file. We listed the items we need designed below 1-4 with a description of what we are looking for below that. We need items 1-4 done with item 5 being optional for you designers. I attached our logo, current business cards, and a picture of real estate for sale sings for reference. Please feel free to email us if you have an questions.

Needs:
1) Logo Redesign.
- I Attached the Logo. I made this logo and need it to be done by a pro.
- I need my logo to be done in high resolution and an illustrator file
- I also need a copy of the logo to fit as my Friendloop background: 851 Wide by 315px Tall

2) Business Cards
- I need business cards design in an illustrator file.
- I need cards designed once with a space for a personal photo and one designed without a personal photo. Personal Photo = A picture of the agent or person.

3) Real Estate For sale signs Designed.
- I need these signs to fit 24”x18”
- Do not say For Sale on them, just have info as listed below
- I would like one design with a space for a personal picture of me, and one designed without a space for a picture
- Need this in an illustrator file

4) Stationary items

5) Some optional items that we could use are:
- Email Signature
- Newsletter template design
- Background design for Chirplet page
- Header and footer. One without contact info and one with contact info
For sale Signs Need: Logo, My Name, 888 #, website.
I do not want them to say “For Sale” on them. I attached a picture of some example signs. I also wouldn’t mind for it to say something in small writing along the lines of “View this home at –or- view details of this home at: CoastlineHomeFinder.example”

Cards need: Logo, Name, Serving All San Diego County, Cell #, Office/Fax#, Email, Website, DRE Lic#.
Backside should have either Logo or say something like “Referrals are the largest complements we can get…” Basically be creative, we could even use it to list all of our social media platforms: Friendloop, Chirplet, Website, Vidstream, Cirqle+.

What to Avoid: Comic / Cartoonish look, but needs to be modern and smooth.

Marcus Tillwater
The Tillwater Group
Real Estate Sales & Investments
Covering All San Diego County “Optional”
Cell: 760-555-0139
Office/Fax 888-555-0162
Marcus@TillwaterGroup.example
www.CoastlineHomeFinder.example
DRE#07392054

Social Media:
http://www.facebook.com/TillwaterGroup
http://www.youtube.com/TillwaterGroup
http://www.yelp.com/biz/the-tillwater-group-oceanside-2

Find us on:
Homevista.example
Parcelly.example
Listingbay.example
Cirqle+
Careernet.example

Target Market(s)

San Diego California Real Estate.

Industry/Entity Type

Real Estate

Requirements
Must have
• 1) Logo Redesign.

2) Business Cards

4) Stationary items
Nice to have
• 5) Some optional items that we could use are:
- Email Signature
Should not have
• Cartoon look.

```html
<!DOCTYPE html>
<html lang="en">
<head>
<meta charset="utf-8">
<title>The Tillwater Group – Business Cards</title>
<link rel="stylesheet" href="https://fonts.googleapis.com/css2?family=Open+Sans:wght@400;600;700&display=swap">
<style>
  :root {
    --backdrop: #3b3b3d;
    --card-white: #ffffff;
    --card-mist: #e9ebef;
    --brand-blue: #1f52a8;
    --brand-navy: #1b2a72;
    --brand-deep: #16205e;
    --ink: #2c2f36;
    --photo-warm: #c99a78;
    --photo-cool: #2c4f86;
  }
  * { box-sizing: border-box; margin: 0; padding: 0; }
  html, body { width: 1200px; height: 900px; overflow: hidden; }
  body {
    background: var(--backdrop);
    font-family: "Open Sans", Arial, sans-serif;
    position: relative;
  }
  .card {
    position: absolute;
    left: 280px;
    width: 640px;
    height: 366px;
    border-radius: 4px;
    overflow: hidden;
    box-shadow: 0 10px 28px rgba(0,0,0,.45);
  }
  /* Back side */
  .card-back {
    top: 52px;
    background: linear-gradient(135deg, var(--brand-blue) 0%, var(--brand-navy) 55%, var(--brand-deep) 100%);
    display: flex;
    flex-direction: column;
    align-items: center;
    justify-content: center;
    color: var(--card-white);
  }
  .card-back .brand-name { font-size: 34px; }
  .card-back .brand-tagline { font-size: 15px; margin-top: 4px; }
  .brand-name {
    font-weight: 600;
    text-transform: uppercase;
    letter-spacing: 2px;
    line-height: 1.1;
  }
  .brand-tagline {
    font-weight: 400;
    letter-spacing: .6px;
  }
  /* Front side */
  .card-front {
    top: 482px;
    background: linear-gradient(160deg, var(--card-white) 40%, var(--card-mist) 100%);
  }
  .front-brand {
    position: absolute;
    right: 36px;
    top: 34px;
    text-align: right;
    color: var(--brand-navy);
  }
  .front-brand .brand-name { font-size: 25px; }
  .front-brand .brand-tagline { font-size: 12.5px; color: var(--brand-deep); margin-top: 2px; }
  .edge-tab {
    position: absolute;
    left: 0;
    top: 150px;
    width: 9px;
    height: 40px;
    background: var(--brand-blue);
    border-radius: 0 4px 4px 0;
  }
  .agent {
    position: absolute;
    left: 40px;
    top: 150px;
    color: var(--ink);
  }
  .agent-name {
    font-size: 17px;
    font-weight: 700;
    color: var(--brand-blue);
    margin-bottom: 18px;
  }
  .agent-line { font-size: 14.5px; line-height: 1.35; }
  .contact-list { list-style: none; margin-top: 8px; }
  .contact-list li {
    display: flex;
    align-items: center;
    gap: 9px;
    font-size: 14.5px;
    line-height: 1.6;
  }
  .contact-list svg { width: 16px; height: 16px; flex: none; }
  .agent-photo {
    position: absolute;
    right: 28px;
    top: 112px;
    width: 170px;
    height: 150px;
    background: radial-gradient(circle at 40% 38%, var(--photo-warm) 0%, #a9896f 35%, var(--photo-cool) 75%);
  }
  .bottom-band {
    position: absolute;
    left: 0;
    bottom: 0;
    width: 640px;
    height: 60px;
  }
</style>
</head>
<body>

<section class="card card-back" aria-label="Business card back">
  <div class="brand-name">The Tillwater Group</div>
  <div class="brand-tagline">Real Estate Sales &amp; Investment</div>
</section>

<section class="card card-front" aria-label="Business card front">
  <div class="front-brand">
    <div class="brand-name">The Tillwater Group</div>
    <div class="brand-tagline">Real Estate Sales &amp; Investment</div>
  </div>

  <div class="edge-tab"></div>

  <div class="agent">
    <div class="agent-name">Marcus Tillwater</div>
    <div class="agent-line">Covering All San Diego County “Optional”</div>
    <div class="agent-line">DRE#07392054</div>
    <ul class="contact-list">
      <li>
        <svg viewBox="0 0 16 16"><circle cx="8" cy="8" r="8" fill="#1f52a8"/><path d="M5.4 4.2l1.3 1.6-.7.9c.5 1 1.3 1.8 2.3 2.3l.9-.7 1.6 1.3-.7 1.3c-2.8-.3-5.2-2.7-5.5-5.5z" fill="#fff"/></svg>
        <span>888-555-0162</span>
      </li>
      <li>
        <svg viewBox="0 0 16 16"><circle cx="8" cy="8" r="8" fill="#1f52a8"/><rect x="5.5" y="3.8" width="5" height="8.4" rx="1" fill="#fff"/><rect x="6.4" y="5" width="3.2" height="4.2" fill="#1f52a8"/></svg>
        <span>760-555-0139</span>
      </li>
      <li>
        <svg viewBox="0 0 16 16"><circle cx="8" cy="8" r="8" fill="#1f52a8"/><rect x="4" y="5.2" width="8" height="5.6" fill="#fff"/><path d="M4 5.2l4 3.2 4-3.2" fill="none" stroke="#1f52a8" stroke-width=".9"/></svg>
        <span>Marcus@TillwaterGroup.example</span>
      </li>
      <li>
        <svg viewBox="0 0 16 16"><circle cx="8" cy="8" r="8" fill="#1f52a8"/><circle cx="8" cy="8" r="4" fill="none" stroke="#fff" stroke-width=".9"/><ellipse cx="8" cy="8" rx="1.8" ry="4" fill="none" stroke="#fff" stroke-width=".8"/><path d="M4 8h8" stroke="#fff" stroke-width=".8"/></svg>
        <span>www.CoastlineHomeFinder.example</span>
      </li>
    </ul>
  </div>

  <div class="agent-photo" role="img" aria-label="Portrait photo of the agent"></div>

  <svg class="bottom-band" viewBox="0 0 640 60" preserveAspectRatio="none" aria-hidden="true">
    <defs>
      <linearGradient id="band-fill" x1="0" x2="1" y1="0" y2="0">
        <stop offset="0" stop-color="#1b2a72"/>
        <stop offset="1" stop-color="#1f52a8"/>
      </linearGradient>
    </defs>
    <polygon points="0,48 640,0 640,60 0,60" fill="url(#band-fill)"/>
  </svg>
</section>

</body>
</html>
```